English and Spanish Language School Needs a Business Card

Need a business card design a startup company called Corvelle Language School. The company will offer English and Spanish conversational level courses designed to make the learner feel comfortable with grammar and vocabulary. We would like to see a logo with some colour that should communicate learning, growth.

Target Market(s)

Consumers and businesses

Industry/Entity Type

Education

Contact Information for Business Card

TBD

Font styles to use
Serif

Requirements
Must have
• Include the following
• Logo
• Name
• Title
• Cellphone Number
• Office Phone number
• Email address
• Office Address

```html
<!DOCTYPE html>
<html lang="en">
<head>
<meta charset="utf-8">
<title>Corvelle Language School – Business Card</title>
<link rel="stylesheet" href="https://fonts.googleapis.com/css2?family=Open+Sans:wght@400;600;700&display=swap">
<style>
  :root {
    --backdrop: #3a3431;
    --card: #1b1b1d;
    --red: #d8313f;
    --teal: #28a4a9;
    --ink: #f2f2f2;
    --muted: #a9a9ab;
    --rule: #8a8a8c;
  }
  * { box-sizing: border-box; margin: 0; padding: 0; }
  html, body { width: 1200px; height: 864px; overflow: hidden; }
  body {
    background: var(--backdrop);
    font-family: "Open Sans", Arial, sans-serif;
    position: relative;
  }
  .card {
    position: absolute;
    width: 560px;
    height: 320px;
    background: var(--card);
    border-radius: 3px;
    box-shadow: 0 10px 28px rgba(0,0,0,.45);
  }
  .card--front { left: 60px; top: 80px; }
  .card--back { left: 580px; top: 464px; }

  .brand {
    position: absolute;
    display: flex;
    align-items: center;
    gap: 10px;
    color: var(--red);
    font-weight: 700;
    white-space: nowrap;
  }
  .brand__dot {
    width: 14px; height: 14px; border-radius: 50%;
    background: var(--teal);
    flex: none;
  }
  .card--front .brand { left: 70px; top: 110px; font-size: 32px; }
  .front__web {
    position: absolute;
    left: 70px; top: 190px;
    color: var(--muted);
    font-size: 14px;
    letter-spacing: 3px;
  }

  .card--back .brand { left: 170px; top: 60px; font-size: 26px; }
  .person {
    position: absolute;
    right: 262px; top: 150px;
    text-align: right;
  }
  .person__name { color: var(--red); font-size: 18px; font-weight: 600; line-height: 1.2; }
  .person__title { color: var(--teal); font-size: 15px; line-height: 1.3; margin-bottom: 10px; }
  .person__address { color: var(--ink); font-size: 14.5px; line-height: 1.45; font-style: normal; }
  .divider {
    position: absolute;
    left: 314px; top: 185px;
    width: 1px; height: 100px;
    background: var(--rule);
  }
  .contacts {
    position: absolute;
    left: 330px; top: 182px;
    list-style: none;
  }
  .contacts li {
    display: flex; align-items: center; gap: 12px;
    color: var(--ink); font-size: 15px; line-height: 26px;
  }
  .contacts svg { width: 14px; height: 14px; flex: none; fill: var(--red); }
</style>
</head>
<body>
  <section class="card card--front">
    <div class="brand"><span class="brand__dot"></span>Corvelle Language School</div>
    <p class="front__web">www.corvellelanguageschool.com</p>
  </section>

  <section class="card card--back">
    <div class="brand"><span class="brand__dot"></span>Corvelle Language School</div>

    <div class="person">
      <p class="person__name">Marta Lindqvist</p>
      <p class="person__title">President</p>
      <address class="person__address">2170 Alderbrook Lane<br>Linden Vale, NY 11480</address>
    </div>

    <div class="divider"></div>

    <ul class="contacts">
      <li>
        <svg viewBox="0 0 16 16" aria-hidden="true"><path d="M2 5c0-2 2-3 6-3s6 1 6 3v1h-3V5H5v1H2z M4 7h8l2 6H2z"/></svg>
        555 0142 7731
      </li>
      <li>
        <svg viewBox="0 0 16 16" aria-hidden="true"><path d="M4 1h8v14H4z M5.5 3v9h5V3z"/></svg>
        555 0187 2264
      </li>
      <li>
        <svg viewBox="0 0 16 16" aria-hidden="true"><path d="M1 3h14v1L8 9 1 4z M1 6l7 5 7-5v7H1z"/></svg>
        marta@corvelle.com
      </li>
      <li>
        <svg viewBox="0 0 16 16" aria-hidden="true"><path d="M8 1a7 7 0 1 0 0 14A7 7 0 0 0 8 1z M8 4a2 2 0 1 1 0 4 2 2 0 0 1 0-4z M5 12c0-2 6-2 6 0z"/></svg>
        www.corvelle.com
      </li>
    </ul>
  </section>
</body>
</html>
```